Velcor Prime Brochure for Chemicals Products

We need a bifold A3 brochure for the exhibition.
you can visit our company website (www.velcorprime.com) for more information about our company.
Company logo and color code attached.
The brochure should contain brief introduction of company, industries, product, and contact (address , telephone and email; joral.k@velcorprime.com)

Product Portfolio:
1. Intermediates
2. Plastics
3. Rubber
4. Additive
5. Fiber
Detail of each products portfolio are in the website. we would like to add product detail but you may help to design how to put it beautifully.

Target Market(s)

Our customers are factories in related industry.

Industry/Entity Type

Automotive, Paint, Electrical Appliance, Tyre and footwear, Textile, Animal Feed, Lubricant

Font styles to use
Sans Serif

Requirements
Must have
• Logo, Product Portfolio for different market.
Nice to have
• prefer curve design rather than rectangular

```html
<!DOCTYPE html>
<html lang="en">
<head>
<meta charset="utf-8">
<title>Velcor Prime Brochure</title>
<link href="https://fonts.googleapis.com/css2?family=Poppins:wght@400;500;600;700;800&display=swap" rel="stylesheet">
<style>
:root{
  --blue:#0a86cf;
  --blue-dark:#0668b0;
  --blue-pale:#dbe7f5;
  --green:#8cc63f;
  --ink:#2b2f36;
  --white:#ffffff;
  --bg:#c9ced8;
}
*{margin:0;padding:0;box-sizing:border-box}
html,body{width:1200px;height:1038px;overflow:hidden;background:var(--bg);font-family:"Poppins",sans-serif;color:var(--ink)}
.spread{position:absolute;left:246px;width:707px;height:500px;overflow:hidden;box-shadow:0 6px 18px rgba(40,50,70,.25);background:var(--white)}
.spread--inside{top:12px}
.spread--outside{top:526px}
.spread svg.art{position:absolute;inset:0;width:707px;height:500px}
.fold{position:absolute;left:353px;top:0;width:1px;height:500px;background:rgba(0,0,0,.08)}
.abs{position:absolute}

/* inside left */
.intro-title{left:26px;top:205px;width:200px;color:var(--white);font-weight:800;font-size:21px;line-height:1.15}
.intro-text{left:26px;top:290px;width:240px;color:var(--white);font-size:7.4px;line-height:1.5}
.stats{left:20px;top:395px;width:270px;display:flex}
.stat{flex:1;text-align:center;color:var(--white);padding:0 4px;border-right:1px solid rgba(255,255,255,.5)}
.stat:last-child{border-right:none}
.stat-icon{width:26px;height:26px;border:1.5px solid var(--white);border-radius:50%;margin:0 auto 4px;display:flex;align-items:center;justify-content:center}
.stat-num{font-weight:800;font-size:15px;line-height:1}
.stat-label{font-weight:600;font-size:6.5px;margin-top:2px}
.stat-note{font-size:5.6px;line-height:1.35;opacity:.9;margin-top:2px}

/* inside right */
.portfolio{left:440px;top:30px;width:248px}
.portfolio h2{font-size:17px;font-weight:800;color:var(--blue);line-height:1.1}
.portfolio h2 span{color:var(--ink)}
.portfolio .lead{font-size:7.2px;line-height:1.45;margin:5px 0 10px}
.product{position:relative;padding-left:16px;margin-bottom:9px}
.product::before{content:"";position:absolute;left:0;top:1px;width:9px;height:9px;border:2px solid var(--green);border-left-color:var(--blue);border-radius:50%}
.product h3{font-size:8.4px;font-weight:700;color:var(--blue);text-transform:uppercase}
.product p{font-size:6.6px;line-height:1.45;margin-top:1px}
.brand{font-weight:700;color:var(--blue);font-size:12px;display:flex;align-items:center;gap:5px}
.brand i{width:9px;height:9px;border-radius:50%;background:var(--green);display:block}
.inside-brand{left:585px;top:452px}
.inside-web{left:440px;top:470px;font-size:7px}

/* outside */
.industries{left:22px;top:150px;width:320px;color:var(--white)}
.industries h2{font-size:16px;font-weight:800;line-height:1.1;margin-bottom:10px}
.industry-list{display:grid;grid-template-columns:1fr 1fr;gap:6px 10px;list-style:none}
.industry-list li{display:flex;align-items:center;gap:6px;font-size:7.4px;line-height:1.15}
.industry-list li::before{content:"";flex:none;width:18px;height:18px;border-radius:50%;background:var(--green);box-shadow:inset 0 0 0 4px var(--green),inset 0 0 0 5.5px var(--white)}
.back-brand{left:26px;top:448px;color:var(--white);font-size:14px}
.back-brand i{background:var(--white)}
.contact{left:200px;top:418px;color:var(--white);font-size:7px;line-height:1.5}
.contact h4{font-size:9px;font-weight:800;letter-spacing:.5px}
.front-brand{left:470px;top:38px;font-size:18px}
.tagline{left:400px;top:78px;width:280px;text-align:center;font-weight:800;font-size:15px;line-height:1.2;color:var(--blue)}
.tagline em{font-style:normal;color:var(--green)}
</style>
</head>
<body>

<section class="spread spread--inside">
  <svg class="art" viewBox="0 0 707 500" aria-hidden="false">
    <defs>
      <clipPath id="photoBand">
        <path d="M300,110 C258,250 270,400 345,500 L430,500 C372,380 372,220 440,0 L380,0 C340,40 315,75 300,110 Z"/>
      </clipPath>
      <linearGradient id="paint" x1="0" x2="1"><stop offset="0" stop-color="#9b3fb0"/><stop offset=".4" stop-color="#e6a11f"/><stop offset=".7" stop-color="#c9321f"/><stop offset="1" stop-color="#9aa3ab"/></linearGradient>
      <linearGradient id="rubber" x1="0" x2="1"><stop offset="0" stop-color="#e9c6b4"/><stop offset="1" stop-color="#d46b8a"/></linearGradient>
    </defs>
    <rect width="353" height="500" fill="var(--blue-pale)"/>
    <g clip-path="url(#photoBand)">
      <rect y="0" width="707" height="130" fill="url(#paint)" role="img" aria-label="Photo of open paint cans in bright colours"/>
      <rect y="130" width="707" height="80" fill="#8ec9de" role="img" aria-label="Photo of a hand holding blue plastic pellets"/>
      <rect y="210" width="707" height="80" fill="url(#rubber)" role="img" aria-label="Photo of a ball of coloured rubber bands"/>
      <rect y="290" width="707" height="85" fill="#c9b9a3" role="img" aria-label="Photo of a laboratory work bench with beakers"/>
      <rect y="375" width="707" height="125" fill="#2b56a6" role="img" aria-label="Photo of blue yarn spools"/>
    </g>
    <path d="M0,165 C90,115 200,95 300,110 C258,250 270,400 345,500 L0,500 Z" fill="var(--blue)" stroke="var(--white)" stroke-width="4"/>
  </svg>
  <div class="fold"></div>

  <h1 class="abs intro-title">We understand our customer's needs</h1>
  <p class="abs intro-text">Established since 2004, Velcor Prime is a specialties chemicals and polymer distribution company serving customers in various industries, including coating, adhesives, automotive, electrical appliances, construction, medical, tyre and rubber, animal feed, and textiles. Our products range from chemical intermediates, engineering plastics, synthetics rubber, additives, fiber and our own tailored made products. At Velcor Prime, our dedicated team thrive on providing innovative solutions and unmatched service to customers.</p>
  <div class="abs stats">
    <div class="stat">
      <div class="stat-icon"><svg width="14" height="12" viewBox="0 0 14 12"><path d="M3 1h8l2 3-6 7-6-7z" fill="none" stroke="#fff" stroke-width="1.2"/></svg></div>
      <div class="stat-num">18+</div>
      <div class="stat-label">Years of experience</div>
      <div class="stat-note">The leaders in the industry with the decade of experience.</div>
    </div>
    <div class="stat">
      <div class="stat-icon"><svg width="14" height="12" viewBox="0 0 14 12"><path d="M1 6l3-3 3 2 3-2 3 3-4 4H5z" fill="none" stroke="#fff" stroke-width="1.2"/></svg></div>
      <div class="stat-num">400+</div>
      <div class="stat-label">Satisfied Clients</div>
      <div class="stat-note">Clients satisfied with our work.</div>
    </div>
    <div class="stat">
      <div class="stat-icon"><svg width="14" height="12" viewBox="0 0 14 12"><path d="M2 3h5v4H2zM7 5h5v5H7z" fill="none" stroke="#fff" stroke-width="1.2"/></svg></div>
      <div class="stat-num">400+</div>
      <div class="stat-label">Blending Products</div>
      <div class="stat-note">Product variety in one contact.</div>
    </div>
  </div>

  <div class="abs portfolio">
    <h2>OUR PRODUCT <span>PORTFOLIO</span></h2>
    <p class="lead">From upstream to downstream, our portfolio covers various polymer related products including customs formulation solutions.</p>
    <div class="product"><h3>Chemicals &amp; Intermediates</h3><p>Our chemicals range from intermediates, monomer, and other products bringing synergy to our client. We offer products to coating resin, ink, adhesive, polyurethane, lubricants, polymer polymerization, textile auxiliaries, etc.</p></div>
    <div class="product"><h3>Plastics</h3><p>We offer polymer and compound materials including short glass fiber, long glass fiber, mineral fillers, conductive, flame retardant, magnetic compound, carbon fiber, color compound and other customs compound, Standard Polymer, Engineering Plastics, Specialties Polymer, Elastomer, Polyurethanes, and Green Polymer.</p></div>
    <div class="product"><h3>Rubber</h3><p>We supply synthetic rubber to major tire producers as well as rubber compounder and converter. Synthetic Rubber, Rubber Compound, Latex, Vulcanizing Agent and Accelerator, Activator and Retarder, Antioxidant, Filler, Wax, Process Oil and Plasticizer.</p></div>
    <div class="product"><h3>Additives</h3><p>We provide wide product range of additives for plastics compound, rubber compound, coating, modified starch and animal feed. We also offer additive masterbatch used for packaging industries: Additives, Oil &amp; Plasticizers, Fillers and Additive Masterbatches.</p></div>
    <div class="product"><h3>Fiber</h3><p>We offer specialties staple fiber and filament yarn for nonwoven, textile spinning, flooring, abrasives, tire cord, and protection fabric. The functionalized products such as antibacteria, flame retardant, biodegradable fiber are also available: Staple Fiber and Filament Yarn.</p></div>
  </div>
  <div class="abs brand inside-brand"><i></i>Velcor Prime</div>
  <div class="abs inside-web">www.velcorprime.com</div>
</section>

<section class="spread spread--outside">
  <svg class="art" viewBox="0 0 707 500">
    <defs>
      <linearGradient id="scene" x1="0" y1="0" x2="1" y2="1"><stop offset="0" stop-color="#5f7f95"/><stop offset=".45" stop-color="#4f8a3a"/><stop offset=".8" stop-color="#3f7a34"/><stop offset="1" stop-color="#6f8fb8"/></linearGradient>
      <linearGradient id="shade" x1="0" x2="1"><stop offset="0" stop-color="#1e3f66" stop-opacity=".85"/><stop offset="1" stop-color="#1e3f66" stop-opacity="0"/></linearGradient>
    </defs>
    <rect width="707" height="500" fill="url(#scene)" role="img" aria-label="Photo of a modern building with rooftop trees and solar panels"/>
    <rect width="360" height="500" fill="url(#shade)"/>
    <path d="M0,0 L707,0 L707,150 C520,200 300,170 0,60 Z" fill="var(--white)"/>
    <path d="M0,405 C230,420 470,350 707,320 L707,500 L0,500 Z" fill="var(--blue)"/>
    <path d="M0,405 C230,420 470,350 707,320" fill="none" stroke="var(--green)" stroke-width="5"/>
  </svg>
  <div class="fold"></div>

  <div class="abs industries">
    <h2>OUR FOCUSED<br>INDUSTRIES</h2>
    <ul class="industry-list">
      <li>Coating</li><li>Health Care</li>
      <li>Agricultural</li><li>Lubricants</li>
      <li>Automotive</li><li>Medical</li>
      <li>Electrical &amp;<br>Electronic</li><li>Packaging</li>
      <li>Construction</li><li>Textile and<br>Footwear</li>
      <li>Consumer<br>Industrial Goods</li><li>Tire and<br>Rubber</li>
      <li>Food &amp; Feeds</li>
    </ul>
  </div>
  <div class="abs brand back-brand"><i></i>Velcor Prime</div>
  <div class="abs contact">
    <h4>SAY HELLO!</h4>
    Joral Kessin<br>
    58/7 Harrow Lane, Riverside Rd., Eastgate District<br>
    Northport 20410<br>
    Tel : +00-12-3456789<br>
    joral.k@velcorprime.com<br>
    www.velcorprime.com
  </div>

  <div class="abs brand front-brand"><i></i>Velcor Prime</div>
  <p class="abs tagline">The <em>Best Value</em> for Business<br>with Perfect Growth</p>
</section>

</body>
</html>
```